Flyer Design

We are a new service called chatvyn.co.uk (see website) This is a premium rate £1:50 per sms text advice service. I am a qualified counsellor who already runs a practice see gavinrowecounselling.uk and have gotten per,it's ion from CALLTARIFFHUB and are registered with them for this service. Quite simply they text Q4 followed by a brief description of their personal dilemma/life or relationship concern to 64915 this is received by me and then I text back with a brief piece of guidance and feedback on their issue. So it is a text based counselling/advice service for those who want a day to day life issue dealt with in confidence,quickly and discreetly. I want the flyers to be basic with a basic and easily transferable and identifiable image like the one on my website.

Industry/Entity Type

Counsellor

```html
<!DOCTYPE html>
<html lang="en">
<head>
<meta charset="utf-8">
<title>Chatvyn Flyer</title>
<link rel="stylesheet" href="https://fonts.googleapis.com/css2?family=Lobster+Two:ital,wght@0,400;0,700;1,400;1,700&display=swap">
<style>
  :root {
    --cyan-light: #6afff3;
    --cyan-mid: #52f2f4;
    --cyan-deep: #38d6f0;
    --star-pale: #c9fbf6;
    --star-edge: #46cfe8;
    --paper: #ffffff;
    --ink-light: #66f6e6;
    --ink-deep: #2bbcee;
  }
  html, body {
    margin: 0;
    padding: 0;
    overflow: hidden;
    background: var(--paper);
  }
  .flyer {
    position: relative;
    width: 1200px;
    height: 850px;
    overflow: hidden;
    background: var(--paper);
    font-family: "Lobster Two", cursive;
    font-weight: 700;
    font-style: italic;
  }
  .bands {
    position: absolute;
    inset: 0;
  }
  .brand-name {
    position: absolute;
    top: 28px;
    left: 0;
    width: 1240px;
    margin: 0;
    text-align: center;
    font-weight: 700;
    font-style: italic;
    font-size: 150px;
    line-height: 1;
    color: var(--paper);
    text-shadow: 0 4px 6px rgba(0, 70, 100, 0.45);
  }
  .price-badge {
    position: absolute;
    left: 40px;
    top: 252px;
    width: 360px;
    height: 360px;
  }
  .price-label {
    position: absolute;
    left: 40px;
    top: 356px;
    width: 360px;
    margin: 0;
    text-align: center;
    font-size: 60px;
    line-height: 1.1;
    color: var(--paper);
    text-shadow: 0 2px 4px rgba(0, 60, 90, 0.5);
  }
  .service-description {
    position: absolute;
    left: 330px;
    top: 282px;
    width: 795px;
    margin: 0;
    text-align: right;
    font-size: 51px;
    line-height: 73px;
    transform: rotate(3deg);
    transform-origin: right top;
    background: linear-gradient(180deg, var(--ink-light), var(--ink-deep));
    -webkit-background-clip: text;
    background-clip: text;
    color: transparent;
  }
  .web-address {
    position: absolute;
    left: 74px;
    top: 748px;
    margin: 0;
    font-size: 64px;
    line-height: 1;
    color: var(--paper);
    text-shadow: 0 3px 5px rgba(0, 70, 100, 0.5);
  }
</style>
</head>
<body>
<main class="flyer">
  <svg class="bands" width="1200" height="850" viewBox="0 0 1200 850" aria-hidden="true">
    <defs>
      <linearGradient id="band-top" x1="0" y1="0" x2="0" y2="1">
        <stop offset="0" stop-color="var(--cyan-deep)"/>
        <stop offset="0.25" stop-color="var(--cyan-light)"/>
        <stop offset="1" stop-color="var(--cyan-mid)"/>
      </linearGradient>
      <linearGradient id="band-bottom" x1="0" y1="0" x2="0" y2="1">
        <stop offset="0" stop-color="var(--cyan-deep)"/>
        <stop offset="0.3" stop-color="var(--cyan-light)"/>
        <stop offset="1" stop-color="var(--cyan-mid)"/>
      </linearGradient>
    </defs>
    <polygon points="0,0 1200,0 1200,228 0,155" fill="url(#band-top)"/>
    <polygon points="0,686 1200,766 1200,850 0,850" fill="url(#band-bottom)"/>
  </svg>

  <h1 class="brand-name">Chatvyn</h1>

  <svg class="price-badge" viewBox="-180 -180 360 360" aria-hidden="true">
    <defs>
      <radialGradient id="badge-fill" cx="0.5" cy="0.3" r="0.75">
        <stop offset="0" stop-color="var(--cyan-light)"/>
        <stop offset="1" stop-color="var(--cyan-deep)"/>
      </radialGradient>
    </defs>
    <g class="badge-outer" fill="var(--star-pale)">
      <rect x="-127" y="-127" width="254" height="254"/>
      <rect x="-127" y="-127" width="254" height="254" transform="rotate(9)"/>
      <rect x="-127" y="-127" width="254" height="254" transform="rotate(18)"/>
      <rect x="-127" y="-127" width="254" height="254" transform="rotate(27)"/>
      <rect x="-127" y="-127" width="254" height="254" transform="rotate(36)"/>
      <rect x="-127" y="-127" width="254" height="254" transform="rotate(45)"/>
      <rect x="-127" y="-127" width="254" height="254" transform="rotate(54)"/>
      <rect x="-127" y="-127" width="254" height="254" transform="rotate(63)"/>
      <rect x="-127" y="-127" width="254" height="254" transform="rotate(72)"/>
      <rect x="-127" y="-127" width="254" height="254" transform="rotate(81)"/>
    </g>
    <g class="badge-inner" fill="var(--star-edge)" transform="rotate(4.5)">
      <rect x="-112" y="-112" width="224" height="224"/>
      <rect x="-112" y="-112" width="224" height="224" transform="rotate(9)"/>
      <rect x="-112" y="-112" width="224" height="224" transform="rotate(18)"/>
      <rect x="-112" y="-112" width="224" height="224" transform="rotate(27)"/>
      <rect x="-112" y="-112" width="224" height="224" transform="rotate(36)"/>
      <rect x="-112" y="-112" width="224" height="224" transform="rotate(45)"/>
      <rect x="-112" y="-112" width="224" height="224" transform="rotate(54)"/>
      <rect x="-112" y="-112" width="224" height="224" transform="rotate(63)"/>
      <rect x="-112" y="-112" width="224" height="224" transform="rotate(72)"/>
      <rect x="-112" y="-112" width="224" height="224" transform="rotate(81)"/>
    </g>
    <circle r="132" fill="url(#badge-fill)"/>
  </svg>
  <p class="price-label">Only<br>£1.50</p>

  <p class="service-description">Chatvyn is a therapy service where<br>you can text your problems or<br>issues to a professional who will<br>help you solve problems, talk to<br>you, and support you through them.</p>

  <p class="web-address">Chatvyn.co.uk</p>
</main>
</body>
</html>
```